German Headhunter/ HR Consultancy needs Business Cards Design

We need a business Card Design for our Company in Stuttgart. We are specialized as Headhunter/ HR Consultancy in Placement of specialist and managers in permanent employment. Please refer to our business logo.

```html
<!DOCTYPE html>
<html lang="de">
<head>
<meta charset="utf-8">
<title>Vektor Personalberatung – Visitenkarte</title>
<link rel="stylesheet" href="https://fonts.googleapis.com/css2?family=Montserrat:wght@400;500;600;700&display=swap">
<style>
  :root {
    --brand-blue: #4a66b6;
    --brand-blue-deep: #3f59ab;
    --ink-grey: #8c8c8c;
    --card-white: #fbfbfb;
    --stage: #ececec;
  }
  * { box-sizing: border-box; margin: 0; padding: 0; }
  html, body {
    width: 1200px; height: 800px; overflow: hidden;
    background: var(--stage);
    font-family: "Montserrat", Arial, sans-serif;
  }
  .sheet {
    width: 1200px; height: 800px;
    display: flex; align-items: center; justify-content: center; gap: 44px;
  }
  .card {
    position: relative;
    width: 540px; height: 309px;
    overflow: hidden;
    box-shadow: 0 10px 24px rgba(0,0,0,0.12);
  }

  /* Front */
  .card--front {
    background: var(--brand-blue);
    display: flex; align-items: center; justify-content: center;
  }
  .brand {
    display: flex; align-items: center; gap: 14px;
  }
  .brand__mark {
    width: 40px; height: 40px; background: currentColor;
  }
  .brand__name {
    font-weight: 700; line-height: 1.05; letter-spacing: 0.04em;
    text-transform: uppercase;
  }
  .card--front .brand { color: #fff; }
  .card--front .brand__name { font-size: 30px; }
  .card--front .brand__name span { display: block; }

  /* Back */
  .card--back { background: var(--card-white); }
  .card--back .brand {
    position: absolute; left: 34px; top: 30px; color: var(--brand-blue-deep);
  }
  .card--back .brand__mark { width: 30px; height: 30px; }
  .card--back .brand__name { font-size: 18px; }
  .card--back .brand__name span { display: block; }

  .holder {
    position: absolute; left: 34px; top: 140px;
  }
  .holder__name {
    font-size: 21px; font-weight: 600; letter-spacing: 0.05em;
    color: var(--brand-blue-deep);
  }
  .holder__role {
    margin-top: 4px; padding-left: 6px;
    font-size: 14px; font-weight: 500; letter-spacing: 0.04em;
    color: var(--ink-grey);
  }
  .divider {
    position: absolute; left: 40px; right: 28px; top: 206px;
    height: 1px; background: var(--brand-blue-deep);
  }
  .contacts {
    position: absolute; left: 42px; top: 218px;
    list-style: none;
  }
  .contacts li {
    display: flex; align-items: center; gap: 10px;
    height: 20px;
    font-size: 11.5px; letter-spacing: 0.03em; color: var(--ink-grey);
  }
  .contacts svg { width: 14px; height: 14px; fill: var(--brand-blue-deep); flex: none; }
  .address {
    position: absolute; right: 28px; top: 214px;
    text-align: right; font-style: normal;
    font-size: 11.5px; line-height: 18px; letter-spacing: 0.03em; color: var(--ink-grey);
  }
  .band {
    position: absolute; left: 0; right: 0; bottom: 0;
    height: 18px; background: var(--brand-blue-deep);
  }
</style>
</head>
<body>
<main class="sheet">

  <section class="card card--front" aria-label="Visitenkarte Vorderseite">
    <div class="brand">
      <div class="brand__mark"></div>
      <div class="brand__name"><span>Vektor</span><span>Personalberatung</span></div>
    </div>
  </section>

  <section class="card card--back" aria-label="Visitenkarte Rückseite">
    <div class="brand">
      <div class="brand__mark"></div>
      <div class="brand__name"><span>Vektor</span><span>Personalberatung</span></div>
    </div>

    <div class="holder">
      <h1 class="holder__name">JONAS BRANDT</h1>
      <p class="holder__role">Owner</p>
    </div>

    <div class="divider"></div>

    <ul class="contacts">
      <li>
        <svg viewBox="0 0 24 24" aria-hidden="true"><path d="M6.6 10.8a15.1 15.1 0 0 0 6.6 6.6l2.2-2.2a1 1 0 0 1 1-.25 11.4 11.4 0 0 0 3.6.57 1 1 0 0 1 1 1V20a1 1 0 0 1-1 1A17 17 0 0 1 3 4a1 1 0 0 1 1-1h3.5a1 1 0 0 1 1 1c0 1.25.2 2.45.57 3.57a1 1 0 0 1-.25 1z"/></svg>
        0711 555 0142
      </li>
      <li>
        <svg viewBox="0 0 24 24" aria-hidden="true"><path d="M2 5h20v14H2zm2 2v.5l8 5 8-5V7zm0 2.9V17h16V9.9l-8 5z"/></svg>
        info@vektorpersonal.de
      </li>
      <li>
        <svg viewBox="0 0 24 24" aria-hidden="true"><path d="M12 2a10 10 0 1 0 0 20 10 10 0 0 0 0-20zm6.9 6h-3a15.6 15.6 0 0 0-1.3-3.6A8 8 0 0 1 18.9 8zM12 4c.8 1.2 1.5 2.5 1.9 4h-3.8c.4-1.5 1.1-2.8 1.9-4zM4.3 14a8.2 8.2 0 0 1 0-4h3.4a16.5 16.5 0 0 0 0 4zm.8 2h3a15.6 15.6 0 0 0 1.3 3.6A8 8 0 0 1 5.1 16zm3-8h-3a8 8 0 0 1 4.3-3.6A15.6 15.6 0 0 0 8.1 8zM12 20c-.8-1.2-1.5-2.5-1.9-4h3.8c-.4 1.5-1.1 2.8-1.9 4zm2.3-6H9.7a14.7 14.7 0 0 1 0-4h4.6a14.7 14.7 0 0 1 0 4zm.3 5.6a15.6 15.6 0 0 0 1.3-3.6h3a8 8 0 0 1-4.3 3.6zM16.3 14a16.5 16.5 0 0 0 0-4h3.4a8.2 8.2 0 0 1 0 4z"/></svg>
        www.vektorpersonal.de
      </li>
    </ul>

    <address class="address">
      Vektor Personalberatung<br>
      Lindenweg 14, Suite 3<br>
      70100 Stuttgart
    </address>

    <div class="band"></div>
  </section>

</main>
</body>
</html>
```